Velvet Harbor small batch hot sauce label project

I am launching a line of small batch sauces (hot sauces, bbq sauces) and I need a label for my bottles. I have a logo that I like, I'm not completely married to it but It is a good logo. I would like the name of my business and the name of the sauce on the label. Something fun, edgy that would make you want to pick it up off the shelf.

Target Market(s)

Milennials, food bloggers, stay at home moms who want to amp up their dishes with a really good sauce

Industry/Entity Type

Cooking

Requirements
Must have
• I am open to interpretation
Nice to have
• Maybe a bomb cloud since I want to go in the sauce bomb direction.

```html
<!DOCTYPE html>
<html lang="en">
<head>
<meta charset="utf-8">
<title>Velvet Harbor Hot Sauce Label</title>
<link rel="stylesheet" href="https://fonts.googleapis.com/css2?family=Bebas+Neue&family=Libre+Baskerville:wght@700&display=swap">
<style>
  :root {
    --canvas: #ffffff;
    --label-orange: #f28a2a;
    --frame-yellow: #f8b21c;
    --panel-black: #0b0b0b;
    --cloud-light: #f7b733;
    --cloud-deep: #e58a1f;
    --cloud-shadow: #3a230a;
    --badge-red: #e31d25;
    --badge-ring: #ffffff;
    --badge-edge: #5b2a12;
    --band-text: #e8461c;
    --sauce-yellow: #f5b42b;
    --white: #ffffff;
    --therm-red: #d9261c;
    --therm-orange: #ef7a1e;
    --therm-amber: #f4a53a;
    --therm-sand: #e7b777;
  }
  html, body {
    margin: 0;
    padding: 0;
    width: 1200px;
    height: 1200px;
    overflow: hidden;
    background: var(--canvas);
  }
  .canvas {
    position: relative;
    width: 1200px;
    height: 1200px;
  }
  .label {
    position: absolute;
    left: 327px;
    top: 44px;
    width: 546px;
    height: 1112px;
    border-radius: 44px;
    background: var(--label-orange);
    box-sizing: border-box;
    padding: 14px;
  }
  .label-frame {
    position: relative;
    width: 100%;
    height: 100%;
    border-radius: 32px;
    background: var(--frame-yellow);
    padding: 12px;
    box-sizing: border-box;
  }
  .label-panel {
    position: relative;
    width: 100%;
    height: 100%;
    border-radius: 22px;
    background: var(--panel-black);
    overflow: hidden;
  }
  .bomb-cloud {
    position: absolute;
    left: 0;
    top: 0;
    width: 100%;
    height: 576px;
    background: linear-gradient(180deg, var(--cloud-light) 0%, var(--cloud-deep) 55%, var(--cloud-shadow) 100%);
  }
  .badge {
    position: absolute;
    left: 50%;
    top: 274px;
    width: 264px;
    height: 264px;
    margin-left: -132px;
    margin-top: -132px;
    border-radius: 50%;
    background: var(--badge-red);
    border: 10px solid var(--badge-ring);
    box-shadow: 0 0 0 6px var(--badge-edge);
    box-sizing: border-box;
    display: flex;
    flex-direction: column;
    align-items: center;
    justify-content: center;
  }
  .badge-line {
    font-family: "Bebas Neue", sans-serif;
    color: var(--white);
    font-size: 90px;
    line-height: 0.8;
    letter-spacing: 1px;
  }
  .name-band {
    position: absolute;
    left: 0;
    top: 576px;
    width: 100%;
    height: 92px;
    background: var(--frame-yellow);
    display: flex;
    align-items: center;
    justify-content: center;
  }
  .brand-name {
    font-family: "Libre Baskerville", serif;
    font-weight: 700;
    font-size: 34px;
    color: var(--band-text);
    letter-spacing: 2px;
    white-space: nowrap;
  }
  .heat-meter {
    position: absolute;
    left: 44px;
    top: 712px;
    width: 64px;
    height: 224px;
  }
  .sauce-name {
    position: absolute;
    left: 120px;
    right: 10px;
    top: 722px;
    text-align: center;
    font-family: "Libre Baskerville", serif;
    font-weight: 700;
    font-size: 40px;
    line-height: 60px;
    color: var(--sauce-yellow);
    margin: 0;
  }
  .net-weight {
    position: absolute;
    left: 110px;
    right: 10px;
    top: 958px;
    text-align: center;
    font-family: "Libre Baskerville", serif;
    font-weight: 700;
    font-size: 32px;
    color: var(--white);
    margin: 0;
  }
</style>
</head>
<body>
<main class="canvas">
  <section class="label">
    <div class="label-frame">
      <div class="label-panel">
        <div class="bomb-cloud" role="img" aria-label="Orange and yellow mushroom cloud of a sauce bomb explosion"></div>

        <div class="badge">
          <span class="badge-line">HOT</span>
          <span class="badge-line">SAUCE</span>
        </div>

        <div class="name-band">
          <span class="brand-name">VELVET HARBOR</span>
        </div>

        <svg class="heat-meter" viewBox="0 0 64 224" aria-label="Heat level meter">
          <rect x="20" y="4" width="24" height="170" rx="4" fill="none" stroke="var(--white)" stroke-width="3"/>
          <rect x="23" y="8" width="18" height="50" fill="var(--therm-red)"/>
          <rect x="23" y="58" width="18" height="38" fill="var(--therm-orange)"/>
          <rect x="23" y="96" width="18" height="38" fill="var(--therm-amber)"/>
          <rect x="23" y="134" width="18" height="38" fill="var(--therm-sand)"/>
          <circle cx="32" cy="198" r="22" fill="var(--therm-red)" role="img" aria-label="Chili pepper"/>
        </svg>

        <h1 class="sauce-name">Habanero<br>Onion<br>Reapers</h1>
        <p class="net-weight">NET WT. 5 oz</p>
      </div>
    </div>
  </section>
</main>
</body>
</html>
```